Business Card Design Project

Double sided business card - logo on one side, my details on the other.

I would like to see two options - my logo on a dark grey/black background and my logo on white.

My details as follows:

Trevan Moulsby MBus, FBQL
P: 0471 562 104
E: trevan@trevanmoulsby.com
W: www.trevanmoulsby.com

Target Market(s)

Managers in business, universities and government.

Industry/Entity Type

Business

Requirements
Must have
• Chirpex, Pagemuro and Vocanet icons

```html
<!DOCTYPE html>
<html lang="en">
<head>
<meta charset="utf-8">
<title>Trevan Moulsby — Business Card Options</title>
<link rel="stylesheet" href="https://fonts.googleapis.com/css2?family=Roboto+Condensed:wght@300;400;700&display=swap">
<style>
  :root {
    --page: #ffffff;
    --dark-edge: #1f1f20;
    --dark-core: #4a4d52;
    --light-edge: #eef0f1;
    --light-core: #fbfbfc;
    --mark-blue: #aab6c8;
    --ink-white: #ffffff;
    --ink-soft-white: #e8e9ea;
    --ink-grey: #6a6a6a;
    --ink-light-grey: #808080;
    --mark-grey: #8d8d8d;
    --icon-tile: #e6e7e8;
    --icon-tile-edge: #d3d4d6;
  }
  * { margin: 0; padding: 0; box-sizing: border-box; }
  html, body { width: 1200px; height: 1000px; overflow: hidden; background: var(--page); }
  body { position: relative; font-family: "Roboto Condensed", "Arial Narrow", sans-serif; }

  .card {
    position: absolute;
    width: 525px;
    height: 300px;
    overflow: hidden;
    box-shadow: 0 8px 18px rgba(0,0,0,0.28);
  }
  .card--dark {
    background: radial-gradient(ellipse 60% 70% at 55% 45%, var(--dark-core), var(--dark-edge) 85%);
  }
  .card--light {
    background: radial-gradient(ellipse 60% 70% at 45% 40%, var(--light-core), var(--light-edge) 90%);
  }
  .card--front-dark { left: 60px; top: 201px; }
  .card--back-light { left: 615px; top: 201px; }
  .card--back-dark  { left: 60px; top: 528px; }
  .card--front-light { left: 615px; top: 528px; }

  .brand { position: absolute; display: flex; align-items: center; }
  .brand__square { background: var(--mark-blue); flex: none; }
  .brand__name { font-weight: 300; line-height: 1; white-space: nowrap; }

  .brand--large .brand__square { width: 90px; height: 90px; margin-right: 26px; }
  .brand--large .brand__name { font-size: 110px; }
  .brand--small .brand__square { width: 40px; height: 40px; margin-right: 12px; }
  .brand--small .brand__name { font-size: 50px; }

  .card--dark .brand__name { color: var(--ink-white); }
  .card--light .brand__name { color: var(--mark-grey); }

  .card--front-dark .brand { left: 60px; top: 95px; }
  .card--front-light .brand { left: 55px; top: 95px; }
  .card--back-light .brand { left: 45px; top: 58px; }
  .card--back-dark .brand { left: 40px; top: 55px; }

  .details { position: absolute; text-align: right; }
  .details__name { font-weight: 700; font-size: 26px; line-height: 1; letter-spacing: -0.2px; }
  .details__credentials { font-size: 6px; margin-top: 2px; }
  .details__contact { list-style: none; margin-top: 26px; font-weight: 300; font-size: 14px; line-height: 19px; }

  .card--back-light .details { right: 95px; top: 150px; color: var(--ink-light-grey); }
  .card--back-light .details__name { color: var(--ink-grey); }
  .card--back-dark .details { right: 96px; top: 150px; color: var(--ink-soft-white); }
  .card--back-dark .details__name { color: var(--ink-white); }

  .social { position: absolute; left: 451px; top: 152px; list-style: none; }
  .social__item { display: flex; align-items: center; height: 18px; margin-bottom: 22px; font-size: 10px; font-weight: 400; color: var(--ink-light-grey); }
  .social__tile { width: 14px; height: 14px; margin-right: 5px; background: var(--icon-tile); border: 1px solid var(--icon-tile-edge); flex: none; }
</style>
</head>
<body>

  <section class="card card--dark card--front-dark" aria-label="Dark card, front">
    <div class="brand brand--large">
      <span class="brand__square"></span>
      <span class="brand__name">Trevan</span>
    </div>
  </section>

  <section class="card card--light card--back-light" aria-label="Light card, back">
    <div class="brand brand--small">
      <span class="brand__square"></span>
      <span class="brand__name">Trevan</span>
    </div>
    <div class="details">
      <p class="details__name">Trevan Moulsby</p>
      <p class="details__credentials">MBus, FBQL</p>
      <ul class="details__contact">
        <li>0471 562 104</li>
        <li>trevan@trevanmoulsby.com</li>
        <li>www.trevanmoulsby.com</li>
      </ul>
    </div>
    <ul class="social">
      <li class="social__item"><span class="social__tile"></span>Vocanet</li>
      <li class="social__item"><span class="social__tile"></span>Pagemuro</li>
      <li class="social__item"><span class="social__tile"></span>Chirpex</li>
    </ul>
  </section>

  <section class="card card--dark card--back-dark" aria-label="Dark card, back">
    <div class="brand brand--small">
      <span class="brand__square"></span>
      <span class="brand__name">Trevan</span>
    </div>
    <div class="details">
      <p class="details__name">Trevan Moulsby</p>
      <p class="details__credentials">MBus, FBQL</p>
      <ul class="details__contact">
        <li>0471 562 104</li>
        <li>trevan@trevanmoulsby.com</li>
        <li>www.trevanmoulsby.com</li>
      </ul>
    </div>
  </section>

  <section class="card card--light card--front-light" aria-label="Light card, front">
    <div class="brand brand--large">
      <span class="brand__square"></span>
      <span class="brand__name">Trevan</span>
    </div>
  </section>

</body>
</html>
```